Business Card Design Project

Design is for the business card of a holistic, integral therapist. Design is required for front (colour / pattern) and back (white, with text as below).

Please prepare the design using placeholder text. I will work with the winning submission to complete the final information in the last iteration.

To give you a sense of her services a profile is below:
- I offer an integrative approach for effective relief of many issues such as anxiety, panic attacks, relationship difficulties, and health problems. In my counselling sessions I mainly use QBR {Quiet Balance Release } which taps into the body's energy system (meridians) to clear up blockages and limiting /distorted thinking and beliefs. I also work on expanding awareness as well as enhancing relationships.Clients have found the sessions life changing and report feeling lighter, clearer more empowered and connected to themselves and others.

Target Market(s)

Well educated, upper socioeconomic people seeking purpose and happiness in their lives.

Industry/Entity Type

Health

Requirements
Must have
• Must have the following text on front

First Name, Last Name
LLB, ND, Dip C
Counselling & Naturopathy
Quiet Balnce Release and Marlow Therapy

Adress 1 Line 1
Adress 1 Line 2

Adress 2 Line 1
Adress 2 Line 2

xxx.xxx@xxxxx.com

Tel: 0XXX XXX XXX

Must have the following text on reverse - which should be primarily white.

Next appointment
Date:
Time:
Nice to have
• Example colour palettes

http://www.huebinder.example/swatch/512093/velvet_lantern
http://www.huebinder.example/swatch/318420/Quiet_Orchard
http://www.huebinder.example/swatch/607215/Morning_Over_Tides

Example images that may be useful...
http://www.shopvarn.example/gp/product/images/4719205536/ref=dp_image_text_0?ie=UTF8&n=517302&s=books
http://www.shopvarn.example/gp/customer-media/product-gallery/6284019573/ref=cm_ciu_pdp_images_all
http://en.loreweb.example/wiki/File:Lotus_Grid_256bw.gif

```html
<!DOCTYPE html>
<html lang="en">
<head>
<meta charset="utf-8">
<title>Business Card – Therapist</title>
<link rel="stylesheet" href="https://fonts.googleapis.com/css2?family=Noto+Sans:wght@400;700&display=swap">
<style>
  :root {
    --band-blue: #3181d6;
    --sky-light: #c6dffa;
    --sky-pale: #e6f1fd;
    --paper: #ffffff;
    --name-white: #ffffff;
    --credential-brown: #5b3b3b;
    --address-grey: #8c8c8c;
    --contact-dark: #3a3a3a;
  }
  html, body {
    margin: 0;
    padding: 0;
    width: 1200px;
    height: 749px;
    overflow: hidden;
    background: var(--paper);
  }
  .card {
    position: relative;
    width: 1200px;
    height: 749px;
    overflow: hidden;
    background: var(--paper);
    font-family: "Noto Sans", Tahoma, sans-serif;
  }
  .card__texture {
    position: absolute;
    inset: 0;
    width: 100%;
    height: 100%;
  }
  .card__band {
    position: absolute;
    left: 0;
    width: 100%;
    background: var(--band-blue);
  }
  .card__band--top { top: 81px; height: 80px; }
  .card__band--bottom { top: 702px; height: 18px; }
  .card__name {
    position: absolute;
    left: 103px;
    top: 104px;
    margin: 0;
    font-size: 29px;
    font-weight: 700;
    line-height: 34px;
    color: var(--name-white);
    white-space: nowrap;
  }
  .card__credentials {
    position: absolute;
    left: 105px;
    top: 226px;
    margin: 0;
    color: var(--credential-brown);
    font-size: 24px;
    line-height: 37px;
    white-space: nowrap;
  }
  .card__address {
    position: absolute;
    left: 116px;
    top: 448px;
    margin: 0;
    font-style: normal;
    color: var(--address-grey);
    font-size: 24px;
    line-height: 41px;
    white-space: nowrap;
  }
  .card__contact {
    position: absolute;
    left: 778px;
    top: 443px;
    margin: 0;
    color: var(--contact-dark);
    font-size: 28px;
    line-height: 46px;
    white-space: nowrap;
  }
  .card__credentials span,
  .card__address span,
  .card__contact span { display: block; }
</style>
</head>
<body>
<div class="card">
  <svg class="card__texture" viewBox="0 0 1200 749" preserveAspectRatio="none" role="img" aria-label="Soft blue halftone dot texture fading from the top right corner">
    <defs>
      <radialGradient id="skyGlow" cx="1200" cy="120" r="1100" gradientUnits="userSpaceOnUse">
        <stop offset="0" stop-color="var(--sky-light)"/>
        <stop offset="0.45" stop-color="var(--sky-pale)"/>
        <stop offset="0.8" stop-color="var(--paper)"/>
      </radialGradient>
    </defs>
    <rect width="1200" height="749" fill="url(#skyGlow)"/>
  </svg>

  <div class="card__band card__band--top"></div>
  <h1 class="card__name">First Name, Last Name</h1>

  <p class="card__credentials">
    <span>LLB, ND, Dip C</span>
    <span>Counselling &amp; Naturopathy</span>
    <span>Quiet Balnce Release and Marlow Therapy</span>
  </p>

  <address class="card__address">
    <span>Adress Demo Samble</span>
    <span>Adress Demo Samble</span>
    <span>Adress Demo Samble</span>
    <span>Adress Demo Samble</span>
  </address>

  <p class="card__contact">
    <span>xxx.xxx@xxxxx.com</span>
    <span>Tel: 0XXX XXX XXX</span>
  </p>

  <div class="card__band card__band--bottom"></div>
</div>
</body>
</html>
```